Bref créative
Logo for coaching business
Bus card design, stationary/letterhead, envelopes
Professional
Gerald Pinsky
Author · Speaker · Guide
20583 W. Marigold Ave. #215-347
Scottsdale, AZ 85917
Gerald@brightkestrelcoaching.example
www.BrightKestrelCoaching.example
Need additional bus. card layout for-
Tom Ridgely, MMAC
Life Coach - Counselor
Tom@brightkestrelcoaching.example

```html
<!DOCTYPE html>
<html lang="en">
<head>
<meta charset="utf-8">
<title>Bright Kestrel Coaching – Business Card</title>
<link href="https://fonts.googleapis.com/css2?family=Cormorant+SC:wght@500;600;700&display=swap" rel="stylesheet">
<style>
  :root {
    --bg: #d9d9db;
    --card: #ffffff;
    --blue: #1f63ad;
    --purple: #8a1f7c;
    --ink: #555a62;
    --shadow: rgba(0,0,0,0.22);
  }
  * { margin: 0; padding: 0; box-sizing: border-box; }
  html, body {
    width: 1200px; height: 864px; overflow: hidden;
    background: var(--bg);
    font-family: "Cormorant SC", "Times New Roman", serif;
  }
  .canvas {
    position: relative; width: 1200px; height: 864px;
    display: flex; align-items: center; justify-content: center; gap: 44px;
  }
  .card {
    position: relative; width: 540px; height: 310px;
    background: var(--card); border-radius: 16px; overflow: hidden;
    box-shadow: 0 14px 30px var(--shadow);
  }
  /* front */
  .card-front {
    display: flex; flex-direction: column; align-items: center; justify-content: center;
  }
  .brand { display: flex; align-items: center; gap: 14px; }
  .brand-dot { width: 46px; height: 46px; border-radius: 50%; background: var(--blue); flex: none; }
  .brand-name { font-weight: 700; font-size: 30px; color: var(--blue); letter-spacing: 1px; }
  .front-url {
    margin-top: 26px; font-size: 13px; font-weight: 600; color: var(--blue);
    letter-spacing: 4px;
  }
  /* back */
  .back-band {
    position: absolute; left: 0; right: 0; bottom: 0; height: 52px;
    background: var(--blue);
  }
  .back-rule {
    position: absolute; left: 0; right: 0; bottom: 60px; height: 3px;
    background: var(--purple);
  }
  .back-brand { position: absolute; left: 34px; top: 30px; display: flex; align-items: center; gap: 12px; }
  .back-brand .brand-dot { width: 38px; height: 38px; }
  .back-brand .brand-name { font-size: 24px; }
  .tagline { font-size: 10.5px; font-weight: 600; color: var(--purple); letter-spacing: 0.6px; }
  .person { position: absolute; left: 34px; top: 108px; width: 230px; }
  .person-name { font-size: 17px; font-weight: 700; color: var(--purple); letter-spacing: 0.5px; }
  .person-title { font-size: 11px; font-weight: 600; color: var(--ink); letter-spacing: 0.5px; margin-top: 2px; }
  .address { margin-top: 14px; font-size: 11px; font-weight: 600; color: var(--ink); line-height: 1.45; }
  .contacts { position: absolute; left: 282px; top: 110px; list-style: none; }
  .contacts li {
    display: flex; align-items: center; gap: 7px;
    font-size: 11px; font-weight: 600; color: var(--ink); line-height: 1; margin-bottom: 7px;
  }
  .contacts svg { width: 13px; height: 13px; flex: none; }
</style>
</head>
<body>
<main class="canvas">

  <section class="card card-front">
    <div class="brand">
      <span class="brand-dot"></span>
      <span class="brand-name">Bright Kestrel Coaching</span>
    </div>
    <p class="front-url">WWW.BRIGHTKESTRELCOACHING.EXAMPLE</p>
  </section>

  <section class="card card-back">
    <div class="back-rule"></div>
    <div class="back-band"></div>

    <div class="back-brand">
      <span class="brand-dot"></span>
      <div>
        <div class="brand-name">Bright Kestrel Coaching</div>
        <div class="tagline">Clear Focus · Steady Growth · Lasting Change</div>
      </div>
    </div>

    <div class="person">
      <div class="person-name">Gerald Pinsky</div>
      <div class="person-title">Author · Speaker · Guide</div>
      <div class="address">20583 W. Marigold Ave. #215-347<br>Cactus Ridge, AZ 85917</div>
    </div>

    <ul class="contacts">
      <li>
        <svg viewBox="0 0 16 16"><circle cx="8" cy="8" r="8" fill="var(--blue)"/><path d="M5.4 4.2l1.4 1.6-.8 1.1c.6 1.2 1.4 2 2.6 2.6l1.1-.8 1.6 1.4-.9 1.3c-3.1-.4-5.9-3.2-6.3-6.3z" fill="#fff"/></svg>
        480-555-0147
      </li>
      <li>
        <svg viewBox="0 0 16 16"><circle cx="8" cy="8" r="8" fill="var(--blue)"/><rect x="4" y="5.2" width="8" height="5.6" fill="#fff"/><path d="M4 5.4l4 3 4-3" fill="none" stroke="var(--blue)" stroke-width="0.9"/></svg>
        Gerald@brightkestrelcoaching.example
      </li>
      <li>
        <svg viewBox="0 0 16 16"><circle cx="8" cy="8" r="8" fill="var(--blue)"/><circle cx="8" cy="8" r="4" fill="none" stroke="#fff" stroke-width="1"/><path d="M4 8h8M8 4c-2 2.5-2 5.5 0 8M8 4c2 2.5 2 5.5 0 8" fill="none" stroke="#fff" stroke-width="0.8"/></svg>
        www.BrightKestrelCoaching.example
      </li>
      <li>
        <svg viewBox="0 0 16 16"><circle cx="8" cy="8" r="8" fill="var(--blue)"/></svg>
        ktremont
      </li>
    </ul>
  </section>

</main>
</body>
</html>
```